Stationary for a Manufacturing Company focused on R&D
Corvane please refer to the concluded Logo Project
Stationary for a Manufacturing Company focused on R&D - Manufacturing
Creative Brief
Use same font as used in my logo
Yes please refer to the log - keep the background colors simple
Modern
Vikram Talwarkar
Stationary for a Manufacturing company
Rustomji Parekh Building, 58 Hill Street, Fortm Mumbai 400019 India
vikram@twin-kay.com
www.corvane.com
The card must show advancement - something different but easy to duplicate.....
no information on the back - maybe just the logo at the back could be ok

```html
<!DOCTYPE html>
<html lang="en">
<head>
<meta charset="utf-8">
<title>Corvane Stationery</title>
<link href="https://fonts.googleapis.com/css2?family=Roboto:wght@400;500&display=swap" rel="stylesheet">
<style>
:root{
  --bg:#efefef;
  --paper:#ffffff;
  --green-dark:#34592f;
  --green:#4f7d45;
  --rule:#c9c9c9;
  --ink:#5a5a5a;
  --ink-soft:#8a8a8a;
  --ghost:#e8ece6;
}
*{margin:0;padding:0;box-sizing:border-box}
html,body{width:1200px;height:936px;overflow:hidden;background:var(--bg)}
.canvas{position:relative;width:1200px;height:936px;font-family:"Roboto",sans-serif;color:var(--ink)}
.sheet{position:absolute;background:var(--paper);box-shadow:0 2px 8px rgba(0,0,0,.12);overflow:hidden}
.swoosh{position:absolute;left:0;top:0;width:100%;display:block}
.wordmark{font-family:"Roboto",sans-serif;font-weight:500;color:var(--ink);white-space:nowrap}
.mark-dot{display:inline-block;border-radius:50%;background:var(--green);flex:none}
.contact{position:absolute;font-size:7px;line-height:1.55;color:var(--ink-soft);white-space:nowrap}

.letterhead{left:173px;top:51px;width:418px;height:639px}
.letterhead .brand{position:absolute;left:14px;top:42px;display:flex;align-items:center;gap:5px}
.letterhead .brand .wordmark{font-size:11px}
.letterhead .ghost-name{position:absolute;left:0;right:0;top:286px;text-align:center;font-family:"Roboto",sans-serif;font-weight:500;font-size:40px;color:var(--ghost)}
.letterhead .contact{left:18px;top:530px}

.folder{left:634px;top:46px;width:462px;height:644px}
.folder .brand{position:absolute;left:0;right:0;top:296px;text-align:center}
.folder .brand .mark-dot{width:46px;height:46px;display:block;margin:0 auto 16px}
.folder .brand .wordmark{font-size:28px}
.folder .rule{width:250px;height:1px;background:var(--rule);margin:8px auto 5px}
.folder .tagline{font-size:8px;letter-spacing:.2em;color:var(--green);text-transform:uppercase}

.card{left:36px;top:738px;width:202px;height:94px}
.card .brand{position:absolute;left:12px;top:24px;display:flex;align-items:center;gap:4px}
.card .brand .wordmark{font-size:9px}
.card .contact{left:12px;top:44px;font-size:5px}
.card-back{left:36px;top:845px;width:202px;height:91px;background:linear-gradient(135deg,var(--green-dark),var(--green));display:flex;align-items:center;justify-content:center}
.card-back .wordmark{font-size:13px;color:#fff}

.envelope{left:264px;top:738px;width:454px;height:198px}
.envelope .brand{position:absolute;left:16px;top:42px;display:flex;align-items:center;gap:5px}
.envelope .brand .wordmark{font-size:11px}
.envelope .contact{left:16px;top:66px;font-size:6px}

.envelope-back{left:736px;top:738px;width:431px;height:198px}
.envelope-back .web{position:absolute;left:0;right:0;top:18px;text-align:center;font-size:8px;letter-spacing:.4em;color:#fff;text-transform:uppercase}
</style>
</head>
<body>
<div class="canvas">

  <section class="sheet letterhead">
    <svg class="swoosh" viewBox="0 0 100 100" preserveAspectRatio="none" style="height:120px">
      <path d="M30,0 L100,0 L100,64 C80,30 58,8 30,0 Z" fill="var(--green)"/>
      <path d="M30,0 C58,10 80,34 100,72" fill="none" stroke="var(--rule)" stroke-width=".6"/>
    </svg>
    <div class="brand"><span class="mark-dot" style="width:12px;height:12px"></span><span class="wordmark">Corvane</span></div>
    <div class="ghost-name">Corvane</div>
    <div class="contact">
      14 Harbour Lane, Camp,<br>
      Pune 411001 India<br>
      Tel +91 20 5550 0101<br>
      Fax +91 20 5550 0102<br>
      info@corvane.com<br>
      www.corvane.com
    </div>
  </section>

  <section class="sheet folder">
    <svg class="swoosh" viewBox="0 0 100 100" preserveAspectRatio="none" style="height:170px">
      <path d="M0,0 L100,0 L100,82 C70,40 35,14 0,8 Z" fill="var(--green)"/>
      <path d="M0,10 C35,18 70,44 100,88" fill="none" stroke="var(--rule)" stroke-width=".5"/>
    </svg>
    <div class="brand">
      <span class="mark-dot"></span>
      <div class="wordmark">Corvane</div>
      <div class="rule"></div>
      <div class="tagline">precision tools</div>
    </div>
  </section>

  <section class="sheet card">
    <svg class="swoosh" viewBox="0 0 100 100" preserveAspectRatio="none" style="height:30px">
      <path d="M35,0 L100,0 L100,90 C78,40 58,10 35,0 Z" fill="var(--green)"/>
    </svg>
    <div class="brand"><span class="mark-dot" style="width:9px;height:9px"></span><span class="wordmark">Corvane</span></div>
    <div class="contact">
      Asha Menon<br>
      Director, Research<br>
      14 Harbour Lane, Pune<br>
      info@corvane.com
    </div>
  </section>

  <section class="sheet card-back">
    <span class="wordmark">Corvane</span>
  </section>

  <section class="sheet envelope">
    <svg class="swoosh" viewBox="0 0 100 100" preserveAspectRatio="none" style="height:70px">
      <path d="M28,0 L100,0 L100,95 C78,45 55,10 28,0 Z" fill="var(--green)"/>
      <path d="M28,0 C55,14 78,50 100,100" fill="none" stroke="var(--rule)" stroke-width=".5"/>
    </svg>
    <div class="brand"><span class="mark-dot" style="width:12px;height:12px"></span><span class="wordmark">Corvane</span></div>
    <div class="contact">
      14 Harbour Lane, Camp, Pune 411001 India<br>
      www.corvane.com
    </div>
  </section>

  <section class="sheet envelope-back">
    <svg class="swoosh" viewBox="0 0 100 100" preserveAspectRatio="none" style="height:110px">
      <path d="M0,0 L100,0 L100,55 C80,70 60,78 40,76 C22,74 10,66 0,58 Z" fill="var(--green)"/>
    </svg>
    <div class="web">www.corvane.com</div>
  </section>

</div>
</body>
</html>
```